Quillory Points website re-design and

the institute of massage therapy is ready for a new website. The current website is around 12 years old and it looks old. Luckily the clients is not against changing the colors so the new design does not have to use the current ugly green color scheme. Be creative! Make it pretty, modern and inviting. The current colors look like mold. Nobody likes mold. I have attached the logo asset file as well as a txt document that details the new website design parameters

1 page

```html
<!DOCTYPE html>
<html lang="en">
<head>
<meta charset="utf-8">
<title>Quillory Institute — Massage Therapy Continuing Education</title>
<link rel="stylesheet" href="https://fonts.googleapis.com/css2?family=Playfair+Display:wght@400;700&family=Lato:wght@300;400;700;900&display=swap">
<style>
:root{
  --pink:#d95f85;
  --pink-soft:#e68aa5;
  --pink-box:#de8aa2;
  --blush:#f6ecef;
  --ink:#1b1b1b;
  --grey:#8a8a8a;
  --tile:#c9c9c9;
  --white:#ffffff;
}
*{box-sizing:border-box;margin:0;padding:0}
html,body{width:1200px;height:4068px;overflow:hidden}
body{font-family:'Lato',sans-serif;color:var(--ink);background:var(--white);position:relative}
.abs{position:absolute}
.serif{font-family:'Playfair Display',serif}

/* top bar */
.topbar{position:absolute;left:0;top:0;width:1200px;height:25px;background:#141414;color:#ddd;font-size:8px;letter-spacing:1px;text-transform:uppercase}
.topbar span{position:absolute;top:8px;display:flex;align-items:center;gap:5px}
.topbar svg{width:8px;height:8px;fill:var(--pink)}

/* nav */
.brand{position:absolute;left:0;top:0;width:224px;height:82px;background:var(--pink);display:flex;align-items:center;gap:10px;padding-left:16px;z-index:3}
.brand-dot{width:12px;height:12px;border-radius:50%;background:var(--white)}
.brand-name{color:var(--white);font-family:'Lato',sans-serif;font-weight:700;font-size:17px;letter-spacing:.5px}
.nav{position:absolute;top:48px;left:0;width:1200px;height:12px;font-size:8px;font-weight:700;letter-spacing:1.5px;text-transform:uppercase}
.nav a{position:absolute;color:var(--ink);text-decoration:none}
.search{position:absolute;border:1px solid #ccc;border-radius:10px;font-size:7px;letter-spacing:1px;color:#aaa;padding:4px 10px;text-transform:uppercase}
.pill{position:absolute;border:1px solid #ccc;border-radius:10px;height:18px;font-size:7px;color:#aaa;display:flex;align-items:center;justify-content:center}
.icon{position:absolute;width:14px;height:14px;fill:none;stroke:var(--ink);stroke-width:1.6}

/* hero */
.hero{position:absolute;left:0;top:82px;width:1200px;height:562px;background:radial-gradient(ellipse 420px 300px at 380px 250px,#f9dbe4 0%,#fdf2f5 55%,#fff 100%)}
.hero-photo{position:absolute;left:690px;top:20px;width:400px;height:540px;border-radius:48% 40% 40% 48%;background:radial-gradient(ellipse at 50% 45%,#e9d8d4 0%,#f6c9d7 45%,rgba(250,220,230,0) 75%)}
.hero-kicker{position:absolute;left:0;width:790px;top:170px;text-align:center;font-size:17px;color:#444}
.hero-title{position:absolute;left:0;width:790px;top:196px;text-align:center;font-family:'Playfair Display',serif;font-weight:700;font-size:52px;line-height:62px;color:var(--pink)}
.btn{position:absolute;height:34px;border-radius:17px;font-size:10px;font-weight:700;display:flex;align-items:center;justify-content:center}
.btn-fill{background:var(--pink);color:var(--white)}
.btn-line{border:1.5px solid var(--pink);color:var(--pink);background:var(--white)}
.arrow{position:absolute;width:34px;height:34px;border-radius:50%;background:#888;opacity:.8;display:flex;align-items:center;justify-content:center;color:#fff;font-size:12px}

/* section headings */
.kicker{position:absolute;left:0;width:1200px;text-align:center;font-size:17px;color:#444}
.heading{position:absolute;left:0;width:1200px;text-align:center;font-family:'Playfair Display',serif;font-size:54px;line-height:62px;color:var(--ink)}

/* packages */
.packages{position:absolute;left:0;top:644px;width:1200px;height:671px;background:radial-gradient(ellipse 380px 220px at 700px 520px,#f8d6e0 0%,var(--blush) 70%)}
.pkg{position:absolute;top:180px;width:345px;height:379px;background:var(--white);border-radius:10px;box-shadow:0 8px 28px rgba(180,120,140,.18);text-align:center}
.pkg .lotus{margin:34px auto 0;width:22px;height:18px;display:block}
.pkg h3{font-weight:700;font-size:20px;margin-top:10px}
.pkg .price{color:var(--pink);font-size:20px;font-weight:700;margin-top:10px}
.pkg p{font-size:14px;line-height:21px;color:var(--grey);font-weight:300;width:150px;margin:22px auto 0}
.pkg .btn{left:102px;top:300px;width:143px}
.btn-dark{background:#111;color:#fff}

/* free course */
.free{position:absolute;left:0;top:1315px;width:1200px;height:338px;background:linear-gradient(100deg,#6c5e80 0%,#4e4464 45%,#2c2533 100%)}
.free-kicker{position:absolute;left:0;width:1200px;top:100px;text-align:center;color:#fff;font-size:17px}
.free-title{position:absolute;left:0;width:1200px;top:125px;text-align:center;font-family:'Playfair Display',serif;font-weight:700;font-size:52px;color:#fff}
.free .btn{left:528px;top:232px;width:144px;background:#fff;color:var(--pink)}

/* courses */
.courses{position:absolute;left:0;top:1653px;width:1200px;height:684px;background:var(--white)}
.cat-title{position:absolute;left:245px;top:190px;font-size:20px;font-weight:700}
.cat-list{position:absolute;left:245px;top:228px;list-style:none;font-size:12px;line-height:22px;color:#333}
.course{position:absolute;width:109px;text-align:center}
.course .thumb{height:83px;background:var(--tile);position:relative}
.course .thumb i{position:absolute;top:25px;width:26px;height:26px;border-radius:50%;border:1.5px solid #fff}
.course .thumb i.fav{left:22px;background:#fff}
.course .thumb i.zoom{left:58px}
.course .stars{color:var(--pink);font-size:8px;letter-spacing:1px;margin-top:4px}
.course .name{font-size:9px;line-height:13px;color:var(--grey);margin-top:2px;padding:0 8px}

/* why */
.why{position:absolute;left:0;top:2337px;width:1200px;height:939px;background:var(--blush)}
.why-card{position:absolute;top:265px;width:229px;height:348px;background:var(--white);border:1.5px solid #efb6c6;border-radius:8px;text-align:center;padding:0 24px}
.why-card .lotus{width:22px;height:18px;display:block;margin:26px auto 0}
.why-card h3{font-size:20px;font-weight:700;line-height:24px;margin-top:8px}
.why-card p{font-size:14px;line-height:21px;color:var(--grey);font-weight:300;margin-top:22px}
.donate{position:absolute;left:245px;top:2975px;width:712px;height:240px;background:var(--pink-box);border-radius:12px;color:#fff;text-align:center;padding:42px 52px 0}
.donate h3{font-size:19px;font-weight:700}
.donate p{font-size:14px;line-height:21px;margin-top:22px}

/* faq */
.faq-title{position:absolute;left:0;width:1200px;top:3330px;text-align:center;font-family:'Playfair Display',serif;font-size:54px}
.faq-sub{position:absolute;left:0;width:1200px;top:3403px;text-align:center;font-size:17px}
.topics-title{position:absolute;left:245px;top:3476px;font-size:20px;font-weight:700}
.topics{position:absolute;left:245px;top:3512px;list-style:none;font-size:15px;line-height:31px;color:#333}
.acc{position:absolute;left:486px;width:471px;height:39px;background:var(--pink-soft);border-radius:10px;color:#fff;font-size:10px;display:flex;align-items:center;padding-left:80px}
.acc::before{content:"+";position:absolute;left:46px;width:16px;height:16px;border-radius:50%;border:1px solid rgba(255,255,255,.8);font-size:12px;display:flex;align-items:center;justify-content:center}
.acc-open{position:absolute;left:486px;top:3522px;width:471px;height:151px;background:#fff;border:1.5px solid #eee;border-radius:10px;padding:14px 80px 0 80px;font-size:10px}
.acc-open::before{content:"–";position:absolute;left:46px;top:12px;width:16px;height:16px;border-radius:50%;background:#f3d4dd;color:var(--pink);display:flex;align-items:center;justify-content:center;font-size:10px}
.acc-open h4{font-size:10px;font-weight:700}
.acc-open p{color:#555;line-height:14px;margin-top:10px}
.faq-wash{position:absolute;left:0;top:3560px;width:420px;height:348px;background:radial-gradient(ellipse at 30% 60%,#f8dde5 0%,rgba(255,255,255,0) 70%)}

/* footer */
.footer{position:absolute;left:0;top:3908px;width:1200px;height:134px;background:#121212;color:#ddd}
.footer .brand-name{position:absolute;left:76px;top:32px;font-size:13px;display:flex;align-items:center;gap:8px}
.footer .line{position:absolute;left:76px;font-size:7px;letter-spacing:1px;text-transform:uppercase;display:flex;gap:5px;align-items:center}
.footer .line svg{width:7px;height:7px;fill:#ddd}
.footer .fnav a{position:absolute;top:71px;font-size:8px;font-weight:700;letter-spacing:1.5px;color:#ddd;text-decoration:none;text-transform:uppercase}
.footer .search{top:67px;left:928px;width:119px;background:#fff;color:#777;border:none}
.footer .pill{top:66px;left:1056px;width:44px;background:#fff;border:none;color:var(--pink)}
.bottom{position:absolute;left:0;top:4042px;width:1200px;height:26px;background:var(--pink);color:#fff;font-size:8px;letter-spacing:.5px;text-align:center;line-height:26px}
</style>
</head>
<body>

<svg width="0" height="0" style="position:absolute">
  <defs>
    <symbol id="lotus" viewBox="0 0 22 18"><path d="M11 1c3 3 3 9 0 14-3-5-3-11 0-14zM1 6c5 0 8 4 10 9-5 0-9-3-10-9zM21 6c-5 0-8 4-10 9 5 0 9-3 10-9z" fill="#d95f85"/></symbol>
    <symbol id="pin" viewBox="0 0 10 10"><path d="M5 0a3.5 3.5 0 0 1 3.5 3.5C8.5 6 5 10 5 10S1.5 6 1.5 3.5A3.5 3.5 0 0 1 5 0z"/></symbol>
    <symbol id="mail" viewBox="0 0 10 10"><path d="M0 2h10v6H0z"/></symbol>
    <symbol id="phone" viewBox="0 0 10 10"><path d="M2 0l2 2-1 2 3 3 2-1 2 2-2 2C4 10 0 6 0 2z"/></symbol>
  </defs>
</svg>

<header>
  <div class="topbar">
    <span style="left:256px"><svg><use href="#pin"/></svg>Your address</span>
    <span style="left:905px"><svg><use href="#mail"/></svg>your@email.com</span>
    <span style="left:1091px"><svg><use href="#phone"/></svg>+123-456-7890</span>
  </div>
  <div class="brand"><span class="brand-dot"></span><span class="brand-name">Quillory Institute</span></div>
  <nav class="nav">
    <a style="left:255px">Home</a>
    <a style="left:315px">Cources ˅</a>
    <a style="left:400px">Guidlines ˅</a>
    <a style="left:490px">FAQs</a>
    <a style="left:545px">Policies</a>
    <a style="left:622px">Contact</a>
    <a style="left:697px">About</a>
  </nav>
  <div class="search" style="left:826px;top:44px;width:121px">Search</div>
  <div class="pill" style="left:955px;top:44px;width:45px">$ ⇅</div>
  <svg class="icon" style="left:1012px;top:46px" viewBox="0 0 14 14"><circle cx="6" cy="6" r="4.5"/><path d="M9.5 9.5 13 13"/></svg>
  <svg class="icon" style="left:1085px;top:46px" viewBox="0 0 14 14"><circle cx="7" cy="4.5" r="3"/><path d="M1.5 13c0-3 2.5-5 5.5-5s5.5 2 5.5 5"/></svg>
  <svg class="icon" style="left:1148px;top:46px;fill:var(--ink);stroke:none" viewBox="0 0 14 14"><path d="M1 3h12l-1.5 8h-9z"/><circle cx="12.5" cy="2" r="2" fill="#d95f85"/></svg>
</header>

<section class="hero">
  <div class="hero-photo" role="img" aria-label="Dancer in a white dress leaping through soft pink smoke"></div>
  <p class="hero-kicker">Committed to Excellence in</p>
  <h1 class="hero-title">Massage Therapy<br>Continuing Education</h1>
  <div class="btn btn-fill" style="left:273px;top:354px;width:114px">Read more</div>
  <div class="btn btn-line" style="left:400px;top:354px;width:115px">Book now</div>
  <div class="arrow" style="left:30px;top:266px">‹</div>
  <div class="arrow" style="left:1135px;top:266px">›</div>
</section>

<section class="packages">
  <p class="kicker" style="top:62px">Popular</p>
  <h2 class="heading" style="top:90px">Packages</h2>
  <div class="pkg" style="left:245px">
    <svg class="lotus"><use href="#lotus"/></svg>
    <h3>Certifications</h3>
    <div class="price">$500-600</div>
    <p>Lorem ipsum dolor sit amet, consetetur sadipscing elitr, sed diam nonumy eirmod tempor invidunt ut</p>
    <div class="btn btn-fill">Book Now</div>
  </div>
  <div class="pkg" style="left:611px">
    <svg class="lotus"><use href="#lotus"/></svg>
    <h3>Shop Our Courses</h3>
    <div class="price">$500-600</div>
    <p>Lorem ipsum dolor sit amet, consetetur sadipscing elitr, sed diam nonumy eirmod tempor invidunt ut</p>
    <div class="btn btn-dark">Book Now</div>
  </div>
</section>

<section class="free" role="img" aria-label="Client relaxing during a facial massage treatment">
  <p class="free-kicker">Take a</p>
  <h2 class="free-title">Free Online Course</h2>
  <div class="btn">Get started</div>
</section>

<section class="courses">
  <p class="kicker" style="top:66px">Available</p>
  <h2 class="heading" style="top:96px">Course Titles</h2>
  <h3 class="cat-title">Category</h3>
  <ul class="cat-list">
    <li>Facial (7)</li><li>Massage (7)</li><li>Packages (7)</li><li>Epics (7)</li><li>Children (7)</li><li>Hands (7)</li><li>Feets (7)</li><li>Pathology (7)</li><li>Law &amp; Rules (7)</li><li>Research (7)</li><li>Others (7)</li>
  </ul>

  <div class="course" style="left:365px;top:193px"><div class="thumb"><i class="fav"></i><i class="zoom"></i></div><div class="stars">★★★★★</div><div class="name">Certified Infant Massage Therapist–Instructor</div></div>
  <div class="course" style="left:486px;top:193px"><div class="thumb"><i class="fav"></i><i class="zoom"></i></div><div class="stars">★★★★★</div><div class="name">Human Trafficking Awareness and Prevention, 2 CEs</div></div>
  <div class="course" style="left:606px;top:193px"><div class="thumb"><i class="fav"></i><i class="zoom"></i></div><div class="stars">★★★★★</div><div class="name">Certified Infant Massage Therapist–Instructor</div></div>
  <div class="course" style="left:728px;top:193px"><div class="thumb"><i class="fav"></i><i class="zoom"></i></div><div class="stars">★★★★★</div><div class="name">Human Trafficking Awareness and Prevention, 2 CEs</div></div>
  <div class="course" style="left:848px;top:193px"><div class="thumb"><i class="fav"></i><i class="zoom"></i></div><div class="stars">★★★★★</div><div class="name">Human Trafficking Awareness and Prevention, 2 CEs</div></div>

  <div class="course" style="left:365px;top:363px"><div class="thumb"><i class="fav"></i><i class="zoom"></i></div><div class="stars">★★★★★</div><div class="name">Certified Infant Massage Therapist–Instructor</div></div>
  <div class="course" style="left:486px;top:363px"><div class="thumb"><i class="fav"></i><i class="zoom"></i></div><div class="stars">★★★★★</div><div class="name">Human Trafficking Awareness and Prevention, 2 CEs</div></div>
  <div class="course" style="left:606px;top:363px"><div class="thumb"><i class="fav"></i><i class="zoom"></i></div><div class="stars">★★★★★</div><div class="name">Certified Infant Massage Therapist–Instructor</div></div>
  <div class="course" style="left:728px;top:363px"><div class="thumb"><i class="fav"></i><i class="zoom"></i></div><div class="stars">★★★★★</div><div class="name">Human Trafficking Awareness and Prevention, 2 CEs</div></div>
  <div class="course" style="left:848px;top:363px"><div class="thumb"><i class="fav"></i><i class="zoom"></i></div><div class="stars">★★★★★</div><div class="name">Human Trafficking Awareness and Prevention, 2 CEs</div></div>
</section>

<section class="why">
  <p class="kicker" style="top:72px">Why the Quillory Institute offer</p>
  <h2 class="heading" style="top:104px">The best online continuing<br>education experience</h2>
  <div class="why-card" style="left:245px">
    <svg class="lotus"><use href="#lotus"/></svg>
    <h3>Instant Access<br>and Results</h3>
    <p>Simply enroll to get instant access to your course. As soon as you pass your test, you can print your certificate instantly. After you finish a course, you can always log back into your account, review the course materials, review your exam results.</p>
  </div>
  <div class="why-card" style="left:485px">
    <svg class="lotus"><use href="#lotus"/></svg>
    <h3>Hassle-<br>Free</h3>
    <p>With our online courses, you work at your own pace. When you log back in, the system will remember where you last left off. After you have completed the exam, you will always have access to course materials.</p>
  </div>
  <div class="why-card" style="left:728px">
    <svg class="lotus"><use href="#lotus"/></svg>
    <h3>Risk free<br>sample course</h3>
    <p>Take a free course to see exactly how our system operates. This gives you the peace of mind of knowing what to expect before you commit to any of our courses. Feel free to see how well you do with an online learning and testing format.</p>
  </div>
</section>
<div class="donate">
  <h3>And if those three reasons aren't enough...</h3>
  <p>We donate 10% of profits to charitable organizations. By doing business with us, you help to support many valuable organizations. We have made donations to Brightpath Camps for Young Readers, Veterans Ride Onward, Unified Games League, Harborline Relief Agency, and many other worthy charities. Thank you for your continued support while together we help these wonderful organizations perform their valuable work.</p>
</div>

<section class="faq">
  <div class="faq-wash" role="img" aria-label="Faint pink smoke wash"></div>
  <h2 class="faq-title">Questions? Look here.</h2>
  <p class="faq-sub">Can't find an answer? Call us at (123) 456 789 or email your@email</p>
  <h3 class="topics-title">Topics</h3>
  <ul class="topics"><li>General</li><li>Trust &amp; safety</li><li>Billing</li><li>Other</li></ul>
  <div class="acc" style="top:3470px">Lorem ipsum dolor sit amet</div>
  <div class="acc-open">
    <h4>Lorem ipsum dolor sit amet</h4>
    <p>Lorem ipsum dolor sit amet, consetetur sadipscing elitr, sed diam nonumy eirmod tempor invidunt ut labore et dolore magna aliquyam erat, sed diam voluptua. At vero eos et</p>
  </div>
  <div class="acc" style="top:3688px">Lorem ipsum dolor sit amet</div>
  <div class="acc" style="top:3741px">Lorem ipsum dolor sit amet</div>
  <div class="acc" style="top:3794px">Lorem ipsum dolor sit amet</div>
</section>

<footer class="footer">
  <div class="brand-name"><span class="brand-dot" style="width:9px;height:9px"></span>Quillory Institute</div>
  <div class="line" style="top:72px"><svg><use href="#pin"/></svg>Your address</div>
  <div class="line" style="top:88px"><svg><use href="#mail"/></svg>your@email.com</div>
  <div class="line" style="top:104px"><svg><use href="#phone"/></svg>+123-456-7890</div>
  <nav class="fnav">
    <a style="left:370px">Home</a><a style="left:431px">Courses</a><a style="left:506px">Guidlines</a><a style="left:586px">FAQs</a><a style="left:641px">Policies</a><a style="left:717px">Contact</a><a style="left:792px">About</a>
  </nav>
  <div class="search">Search</div>
  <div class="pill">$ ⇅</div>
</footer>
<div class="bottom">© Copyright 2022 Your Company. All right reserved.</div>

</body>
</html>
```